Brackenfield Carpets Ltd

I'm looking for a modern looking business card with a logo that's relates to the business, maybe a sheep etc. I will need my name and phone numbers to be included

Industry/Entity Type

Business

Contact Information for Business Card

Tom Brackenfield, Director
Phone numbers mobile 07913 546208 and office 0161 735 2846
Carpets and flooring supplied and fitted

```html
<!DOCTYPE html>
<html lang="en">
<head>
<meta charset="utf-8">
<title>Brackenfield Carpets Ltd – Business Card</title>
<link href="https://fonts.googleapis.com/css2?family=Oswald:wght@400;500&family=Michroma&display=swap" rel="stylesheet">
<style>
  :root {
    --backdrop: #c6c6c6;
    --card-dark: #1c1c1e;
    --card-mid: #3a3a3d;
    --crimson: #9c1c41;
    --silver: #d2d2d2;
    --ink-light: #e6e6e6;
  }
  * { margin: 0; padding: 0; box-sizing: border-box; }
  html, body { width: 1200px; height: 1200px; overflow: hidden; }
  body { background: var(--backdrop); position: relative; font-family: "Oswald", sans-serif; }

  .card {
    position: absolute;
    width: 840px;
    height: 528px;
    border-radius: 22px;
    overflow: hidden;
    background: radial-gradient(ellipse at 50% 45%, var(--card-mid) 0%, #26262a 45%, var(--card-dark) 100%);
    box-shadow: 0 2px 6px rgba(0,0,0,0.35);
  }
  .card-front { left: 118px; top: 45px; }
  .card-back { left: 300px; top: 617px; }

  .corner-bands { position: absolute; inset: 0; width: 100%; height: 100%; }

  .brand-mark {
    position: absolute;
    display: flex;
    flex-direction: column;
    align-items: center;
  }
  .brand-square {
    background: var(--crimson);
    border-radius: 16px;
  }
  .brand-name {
    color: var(--ink-light);
    font-weight: 400;
    text-transform: uppercase;
    text-align: center;
    line-height: 1.1;
    letter-spacing: 3px;
  }

  .card-front .brand-mark { left: 95px; top: 153px; width: 310px; }
  .card-front .brand-square { width: 138px; height: 138px; margin-bottom: 20px; }
  .card-front .brand-name { font-size: 34px; }

  .card-back .brand-mark { left: 220px; top: 124px; width: 400px; }
  .card-back .brand-square { width: 174px; height: 174px; margin-bottom: 28px; border-radius: 20px; }
  .card-back .brand-name { font-size: 44px; }

  .divider {
    position: absolute;
    left: 420px; top: 125px;
    width: 3px; height: 280px;
    background: var(--crimson);
  }

  .contact { position: absolute; left: 454px; top: 140px; }
  .person-name {
    color: var(--ink-light);
    font-size: 50px;
    font-weight: 500;
    line-height: 1;
    letter-spacing: 0.5px;
  }
  .person-role {
    font-family: "Michroma", sans-serif;
    color: var(--crimson);
    font-size: 19px;
    letter-spacing: 7px;
    margin-top: 12px;
    margin-bottom: 14px;
  }
  .contact-line {
    display: flex;
    align-items: center;
    color: #ffffff;
    font-size: 30px;
    height: 51px;
  }
  .contact-icon { width: 26px; height: 26px; margin-right: 16px; fill: var(--crimson); }
</style>
</head>
<body>

<section class="card card-front">
  <svg class="corner-bands" viewBox="0 0 840 528" aria-hidden="true">
    <polygon points="0,0 312,0 0,177" fill="var(--crimson)"/>
    <line x1="0" y1="177" x2="312" y2="0" stroke="#8a8a8a" stroke-width="4"/>
    <polygon points="840,350 840,528 522,528" fill="var(--silver)"/>
    <line x1="522" y1="528" x2="840" y2="350" stroke="#8a8a8a" stroke-width="4"/>
  </svg>

  <div class="brand-mark">
    <div class="brand-square"></div>
    <p class="brand-name">Brackenfield<br>Carpets Ltd</p>
  </div>

  <div class="divider"></div>

  <div class="contact">
    <h1 class="person-name">Tom Brackenfield</h1>
    <p class="person-role">DIRECTOR</p>
    <p class="contact-line">
      <svg class="contact-icon" viewBox="0 0 24 24" aria-hidden="true"><path d="M7 1h10a2 2 0 0 1 2 2v18a2 2 0 0 1-2 2H7a2 2 0 0 1-2-2V3a2 2 0 0 1 2-2zm0 3v14h10V4z"/></svg>
      07913 546208
    </p>
    <p class="contact-line">
      <svg class="contact-icon" viewBox="0 0 24 24" aria-hidden="true"><path d="M2 8c0-3 4-5 10-5s10 2 10 5v2h-5V7.5H7V10H2zM5 12h14l2 9H3zm7 2a3 3 0 1 0 0 6 3 3 0 0 0 0-6z"/></svg>
      0161 735 2846
    </p>
    <p class="contact-line">
      <svg class="contact-icon" viewBox="0 0 24 24" aria-hidden="true"><path d="M2 5h20v14H2zm2 2v1l8 5 8-5V7l-8 5z"/></svg>
      Email
    </p>
  </div>
</section>

<section class="card card-back">
  <div class="brand-mark">
    <div class="brand-square"></div>
    <p class="brand-name">Brackenfield<br>Carpets Ltd</p>
  </div>
</section>

</body>
</html>
```